Vexo App

We want to have a web banner (4-5 slides) flash or whatever.
We are innovative next generation messenger with a good design, themes, snap mode, pinging and other features.
Inspired by night, by techno music, by energy, by innovations and next generation.
High tech.

The name of the app : Vexo
vexoapp.example

The banner will be used for nightlisting.example

We want the banner to be creative, and deliver the inspiration of the app.

All the assets, logos and so on can me delivered to you via email by request.

```html
<!DOCTYPE html>
<html lang="en">
<head>
<meta charset="utf-8">
<title>Vexo – Inspired by night</title>
<link href="https://fonts.googleapis.com/css2?family=Montserrat:wght@600;700&display=swap" rel="stylesheet">
<style>
  :root {
    --stage: #525b63;
    --banner-dark: #2f4a06;
    --banner-mid: #6f9a10;
    --banner-light: #b4d12a;
    --banner-edge: #ffffff;
    --text-light: #ffffff;
    --brand-square: #5ab8f2;
    --button-top: #a6e6fb;
    --button-bottom: #3fb2e6;
    --button-border: #e6f8ff;
    --button-text: #15303d;
  }
  * { box-sizing: border-box; margin: 0; padding: 0; }
  html, body {
    width: 1200px;
    height: 900px;
    overflow: hidden;
    background: var(--stage);
    font-family: "Montserrat", Arial, sans-serif;
  }
  .banner {
    position: absolute;
    left: 52px;
    top: 381px;
    width: 1096px;
    height: 138px;
    border: 1px solid var(--banner-edge);
    overflow: hidden;
  }
  .banner-backdrop {
    position: absolute;
    inset: 0;
    background:
      radial-gradient(ellipse 180px 90px at 84% 70%, rgba(220,240,80,0.55), transparent 70%),
      radial-gradient(ellipse 260px 110px at 22% 20%, rgba(190,220,50,0.45), transparent 70%),
      linear-gradient(180deg, var(--banner-mid) 0%, var(--banner-dark) 45%, var(--banner-mid) 75%, var(--banner-light) 100%);
  }
  .brand {
    position: absolute;
    left: 22px;
    top: 19px;
    display: flex;
    align-items: center;
    gap: 26px;
  }
  .brand-square {
    width: 92px;
    height: 80px;
    background: var(--brand-square);
    border-radius: 8px;
  }
  .brand-name {
    color: var(--text-light);
    font-weight: 700;
    font-size: 52px;
    letter-spacing: -1px;
  }
  .message {
    position: absolute;
    left: 347px;
    top: 6px;
    color: var(--text-light);
  }
  .headline {
    font-weight: 700;
    font-size: 50px;
    line-height: 62px;
    letter-spacing: -0.5px;
  }
  .subline {
    font-weight: 600;
    font-size: 21px;
    line-height: 33px;
  }
  .cta {
    position: absolute;
    left: 864px;
    top: 37px;
    width: 206px;
    height: 70px;
    border: 2px solid var(--button-border);
    border-radius: 9px;
    background: linear-gradient(180deg, var(--button-top), var(--button-bottom));
    color: var(--button-text);
    font-family: "Montserrat", Arial, sans-serif;
    font-weight: 600;
    font-size: 26px;
    display: flex;
    align-items: center;
    justify-content: center;
    text-decoration: none;
  }
</style>
</head>
<body>
  <div class="banner">
    <div class="banner-backdrop" role="img" aria-label="Glowing green tiled light grid, like a night club floor"></div>
    <div class="brand">
      <span class="brand-square"></span>
      <span class="brand-name">Vexo</span>
    </div>
    <div class="message">
      <h1 class="headline">Inspired by night!</h1>
      <p class="subline">New groundbreaking messenger<br>for your mobile now available!</p>
    </div>
    <a class="cta" href="#">Try it now!</a>
  </div>
</body>
</html>
```